BrightWink Boothery Business Card Design Project

BrightWink Boothery requires a business card design. We hire PhotoBooths to events such as Birthday Parties, Hens and Bucks Night, Anniversaries, Corporate Functions
, Engagements, Theme Nights, Presentation Night etc.
Business Card needs to look Modern, Professional And Catchy.
Updates

Hello Thankyou for all of your great designs, contact information will be provided shortly. We are considering the front of the card to be white themed and the back of the card to be black themed. And all social media colours to be their original colour. Thankyou

Hello everyone, Here are the contact details: Colin Marsh - Manager Mobile number - 0491838047 Website - www.brightwinkboothery.com Email - admin@brightwinkboothery.com And if you can add the word "weddings" in the "We cater For" section would be good. Thankyou

Target Market(s)

Birthday Parties
Hens and Bucks Night
Weddings
Corporate Functions
Engagements
Theme Nights
Presentation Night
School Functions

Industry/Entity Type

Events

Requirements
Must have
• Must Match Logo
Must Have www.brightwinkboothery.com

On Back of card must have social media icons Facebook, Twitter, Youtube, Linkin and

We Cater For:

Birthday Parties
Hens and Bucks Night
Anniversaries
Corporate Functions
Engagements
Theme Nights
Presentation Night
School Functions
And more.....

```html
<!DOCTYPE html>
<html lang="en">
<head>
<meta charset="utf-8">
<title>BrightWink Boothery – Business Cards</title>
<link rel="stylesheet" href="https://fonts.googleapis.com/css2?family=Open+Sans:wght@400;600;700&display=swap">
<style>
  :root {
    --bg: #e9e6e2;
    --card: #ffffff;
    --ink: #3a3a3a;
    --ink-dark: #1d1d1d;
    --blue: #29a3dd;
    --blue-deep: #1a8fd0;
    --black-band: #222222;
    --muted: #777777;
  }
  * { margin: 0; padding: 0; box-sizing: border-box; }
  html, body { width: 1200px; height: 913px; overflow: hidden; }
  body {
    background: var(--bg);
    font-family: "Open Sans", Arial, sans-serif;
    color: var(--ink);
    position: relative;
  }
  .card {
    position: absolute;
    width: 540px;
    height: 309px;
    background: var(--card);
    box-shadow: 0 6px 18px rgba(0,0,0,.18);
    overflow: hidden;
  }
  .card--services { left: 40px; top: 190px; }
  .card--contact { left: 620px; top: 414px; }

  .brand { display: flex; align-items: center; gap: 12px; position: absolute; }
  .brand__dot { width: 34px; height: 34px; border-radius: 50%; background: var(--blue); }
  .brand__name { font-size: 34px; font-weight: 700; color: var(--ink-dark); letter-spacing: -.5px; line-height: 1; }

  .card--services .brand { left: 80px; top: 62px; }
  .services__title {
    position: absolute; left: 0; right: 0; top: 134px;
    text-align: center; color: var(--blue); font-size: 15px;
  }
  .services__list {
    position: absolute; left: 40px; right: 30px; top: 166px;
    list-style: none; font-size: 15.5px; color: var(--ink); line-height: 30px;
  }
  .services__row span::before { content: "» "; color: var(--blue); font-weight: 700; }
  .services__row span + span { margin-left: 12px; }
  .services__row:nth-child(2) { padding-left: 24px; }
  .services__row:nth-child(3) { padding-left: 48px; }

  .card--contact .brand { left: 40px; top: 104px; }
  .person { position: absolute; right: 36px; top: 54px; text-align: right; }
  .person__name { font-size: 14px; font-weight: 700; color: var(--ink); }
  .person__role { font-size: 10px; color: var(--muted); }
  .social { position: absolute; right: 36px; top: 160px; display: flex; gap: 8px; }
  .social__tile { width: 22px; height: 22px; background: var(--blue); }

  .bands { position: absolute; left: 0; top: 0; }
  .website {
    position: absolute; right: 26px; top: 246px;
    color: #ffffff; font-size: 12px; letter-spacing: .3px;
  }
  .contact-list {
    position: absolute; left: 22px; top: 240px;
    list-style: none; color: #ffffff; font-size: 11.5px; line-height: 19px;
  }
  .contact-list li { display: flex; align-items: center; gap: 6px; }
  .contact-list svg { width: 11px; height: 11px; flex: none; }
  .contact-list .gap { margin-left: 14px; }
</style>
</head>
<body>

<section class="card card--services" aria-label="Card back: services">
  <div class="brand">
    <span class="brand__dot"></span>
    <span class="brand__name">BrightWink Boothery</span>
  </div>
  <p class="services__title">We Cater For:</p>
  <ul class="services__list">
    <li class="services__row"><span>Birthday Parties</span><span>Hens and Bucks Night</span><span>Anniversaries</span></li>
    <li class="services__row"><span>Corporate Functions</span><span>Engagements</span><span>Theme Nights</span></li>
    <li class="services__row"><span>Presentation Night</span><span>School Functions</span><span>And more.....</span></li>
  </ul>
</section>

<section class="card card--contact" aria-label="Card front: contact">
  <svg class="bands" width="540" height="309" viewBox="0 0 540 309" aria-hidden="true">
    <polygon points="300,200 540,200 540,309 300,309" fill="var(--black-band)"/>
    <polygon points="0,232 318,232 352,309 0,309" fill="var(--blue)"/>
    <polygon points="0,300 352,300 356,309 0,309" fill="var(--blue-deep)"/>
  </svg>

  <div class="person">
    <p class="person__name">Your Long Name</p>
    <p class="person__role">Managing Director</p>
  </div>

  <div class="social" aria-label="Social media">
    <span class="social__tile"></span>
    <span class="social__tile"></span>
    <span class="social__tile"></span>
    <span class="social__tile"></span>
  </div>

  <div class="brand">
    <span class="brand__dot"></span>
    <span class="brand__name">BrightWink Boothery</span>
  </div>

  <p class="website">www.brightwinkboothery.com</p>

  <ul class="contact-list">
    <li>
      <svg viewBox="0 0 12 12"><path d="M2 1h3l1 3-2 1c.6 1.4 1.6 2.4 3 3l1-2 3 1v3c-5 .5-9.5-4-9-9z" fill="#fff"/></svg>
      000 0 0 000 00
      <svg class="gap" viewBox="0 0 12 12"><rect x="1" y="4" width="10" height="7" fill="#fff"/><rect x="3" y="1" width="6" height="3" fill="#fff"/></svg>
      (03) 9417 2265
    </li>
    <li>
      <svg viewBox="0 0 12 12"><rect x="1" y="2.5" width="10" height="7" fill="#fff"/><path d="M1 3l5 4 5-4" stroke="var(--blue)" fill="none"/></svg>
      yourname@yourwebsite.com
    </li>
    <li>
      <svg viewBox="0 0 12 12"><path d="M6 11C3 7 2 5.5 2 4.2a4 4 0 0 1 8 0C10 5.5 9 7 6 11z" fill="#fff"/><circle cx="6" cy="4.3" r="1.4" fill="var(--blue)"/></svg>
      Your long commercial of office address
    </li>
  </ul>
</section>

</body>
</html>
```